FR banner

we need a banner design (36"x120" horizontal) that will be displayed on a local high school baseball field. My company ( Crestwell Prints Co) has been producing signage for the Fernmoor Ridge community since 2009. We would like to communicate that we do more than banners. The final design should include the slogan "Signs Shirts Swag" and our Logo.

Target Market(s)

companies, teams, events, shirt and other marketing items.

Industry/Entity Type

Sign, Print,

Font styles to use
Sans Serif

Requirements
Should not have
• no baseball content.

```html
<!DOCTYPE html>
<html lang="en">
<head>
<meta charset="utf-8">
<title>Crestwell Prints Co — Fernmoor Ridge Banner</title>
<link href="https://fonts.googleapis.com/css2?family=Alfa+Slab+One&family=Luckiest+Guy&display=swap" rel="stylesheet">
<style>
  :root {
    --red: #e10012;
    --white: #ffffff;
    --yellow: #ffe500;
    --green: #0b5a2e;
    --ink: #050505;
    --photo-dark: #1c1c1e;
    --photo-mid: #3a3b40;
  }
  html, body {
    margin: 0;
    padding: 0;
    width: 1200px;
    height: 4000px;
    overflow: hidden;
    background: var(--white);
  }
  .banner {
    position: relative;
    width: 1200px;
    height: 4000px;
    background: var(--white);
    overflow: hidden;
  }
  .top-band {
    position: absolute;
    left: 0; top: 0;
    width: 1200px;
    height: 226px;
    background: var(--red);
    border-radius: 0 0 155px 155px;
  }
  .brand {
    position: absolute;
    left: 0; top: 357px;
    width: 1200px;
    height: 932px;
  }
  .brand text {
    font-family: "Alfa Slab One", sans-serif;
    fill: var(--ink);
  }
  .message-panel {
    position: absolute;
    left: 0; top: 1421px;
    width: 1200px;
    height: 2100px;
    background: var(--red);
    border-radius: 155px 155px 0 0;
  }
  .copy {
    position: absolute;
    left: 0; top: 0;
    width: 1200px;
    height: 4000px;
  }
  .headline {
    font-family: "Alfa Slab One", sans-serif;
  }
  .headline .white { fill: var(--white); }
  .headline .yellow { fill: var(--yellow); }
  .slogan {
    font-family: "Luckiest Guy", sans-serif;
    filter: drop-shadow(16px 14px 0 var(--green));
  }
  .slogan .white { fill: var(--white); }
  .slogan .yellow { fill: var(--yellow); }
  .lifestyle-photo {
    position: absolute;
    left: 0; top: 3487px;
    width: 1200px;
    height: 513px;
    background: linear-gradient(180deg, var(--photo-mid) 0%, var(--photo-dark) 100%);
  }
</style>
</head>
<body>
  <main class="banner">
    <div class="top-band"></div>

    <svg class="brand" viewBox="0 0 1200 932" aria-label="Crestwell Prints Co">
      <text x="600" y="430" text-anchor="middle" font-size="170" textLength="1020" lengthAdjust="spacingAndGlyphs">CRESTWELL</text>
      <text x="600" y="640" text-anchor="middle" font-size="170" textLength="860" lengthAdjust="spacingAndGlyphs">PRINTS CO</text>
    </svg>

    <section class="message-panel"></section>

    <svg class="copy" viewBox="0 0 1200 4000">
      <g class="headline">
        <text class="white" x="85" y="1747" font-size="250" textLength="1040" lengthAdjust="spacingAndGlyphs">WE DO</text>
        <text class="white" x="85" y="1871" font-size="140" textLength="1040" lengthAdjust="spacingAndGlyphs">MORE THAN</text>
        <text class="yellow" x="85" y="2027" font-size="186" textLength="1040" lengthAdjust="spacingAndGlyphs">BANNERS</text>
      </g>
      <g class="slogan">
        <text class="white" x="95" y="2548" font-size="430" textLength="1020" lengthAdjust="spacingAndGlyphs">SIGNS</text>
        <text class="yellow" x="95" y="2922" font-size="470" textLength="1010" lengthAdjust="spacingAndGlyphs">SHIRTS</text>
        <text class="white" x="95" y="3282" font-size="430" textLength="1005" lengthAdjust="spacingAndGlyphs">SWAG</text>
      </g>
    </svg>

    <div class="lifestyle-photo" role="img" aria-label="Photo of two people in dark printed t-shirts and sunglasses in front of a dark brick wall"></div>
  </main>
</body>
</html>
```